Email Signature Design (GIF)

I need an Email Signature designed, In a GIF format. The following Excel File and Logo Image should be applied. The Logo on the left and the Fixed "Supplying" and rotating words amongst the variety appears on the right.
e.g. "(HM LOGO) Supplying (Variant)" . Please us the Vorquo screenshots, only as an example.

Target Market(s)

Our current customer base (Construction)

Industry/Entity Type

Construction

Font styles to use
Sans Serif

Requirements
Must have
• My project Must follow the instructions in the Project description

```html
<!DOCTYPE html>
<html lang="en">
<head>
<meta charset="UTF-8">
<title>Hartmoor Materials – Email Signature</title>
<link href="https://fonts.googleapis.com/css2?family=Poppins:wght@400;700&display=swap" rel="stylesheet">
<style>
  :root {
    --backdrop: #b9b9b9;
    --card: #ffffff;
    --navy: #1c2a5e;
    --orange: #ee7d2e;
    --headline: #2b4f86;
  }
  html, body {
    margin: 0;
    padding: 0;
    width: 1200px;
    height: 900px;
    overflow: hidden;
    background: var(--backdrop);
  }
  .canvas {
    position: relative;
    width: 1200px;
    height: 900px;
    background: var(--backdrop);
  }
  .signature {
    position: absolute;
    left: 180px;
    top: 292px;
    width: 900px;
    height: 150px;
    background: var(--card);
    box-sizing: border-box;
    display: flex;
    align-items: center;
  }
  .edge {
    position: absolute;
    top: 0;
    bottom: 0;
    width: 10px;
    display: flex;
  }
  .edge span { display: block; height: 100%; }
  .edge .navy { width: 6px; background: var(--navy); }
  .edge .orange { width: 4px; background: var(--orange); }
  .edge-left { left: 0; }
  .edge-right { right: 0; }
  .brand {
    position: absolute;
    left: 38px;
    top: 50%;
    transform: translateY(-50%);
    width: 180px;
    display: flex;
    align-items: center;
    gap: 10px;
  }
  .brand-dot {
    width: 14px;
    height: 14px;
    border-radius: 50%;
    background: var(--orange);
    flex: none;
  }
  .brand-name {
    font-family: "Poppins", sans-serif;
    font-weight: 700;
    font-size: 22px;
    line-height: 1.05;
    color: var(--navy);
  }
  .tagline {
    position: absolute;
    left: 234px;
    top: 50%;
    transform: translateY(-54%);
    margin: 0;
    font-family: "Poppins", sans-serif;
    font-weight: 400;
    font-size: 48px;
    letter-spacing: 0.3px;
    color: var(--headline);
    white-space: nowrap;
  }
  .tagline .variant { margin-left: 14px; }
</style>
</head>
<body>
  <div class="canvas">
    <div class="signature">
      <div class="edge edge-left"><span class="navy"></span><span class="orange"></span></div>
      <div class="brand">
        <span class="brand-dot"></span>
        <span class="brand-name">Hartmoor<br>Materials</span>
      </div>
      <p class="tagline">Supplying<span class="variant">Wash Sands</span></p>
      <div class="edge edge-right"><span class="orange"></span><span class="navy"></span></div>
    </div>
  </div>
</body>
</html>
```